Host Home Needed Flier

We need a refresh of this flier to be more modern and informative. We'll use the new flier as a template for all our centers across the United States-therefore, it should be editable. We don't typically use stock photos (in order to look authentic to our clients) be would be open to a stock photo if it was relevant. We have a lot of work coming up and would like to establish a relationship with a designer. We are an international company who have been business for over 30 years working with international students ages 8-30. Our marketing/branding colors should be fresh and appeal to young people from all over the globe. We love the color blue in every shade and we love innovative cool fonts.

```html
<!DOCTYPE html>
<html lang="en">
<head>
<meta charset="utf-8">
<title>Host Home Needed Flier</title>
<link href="https://fonts.googleapis.com/css2?family=Montserrat:wght@300;400;700&family=PT+Sans:wght@700&display=swap" rel="stylesheet">
<style>
  :root {
    --mat: #1c1816;
    --header-a: #0b4a8a;
    --header-b: #2d6a78;
    --sky: #14aee0;
    --sky-deep: #1c8fc4;
    --slate: #3a7aa6;
    --band-a: #2a8fc4;
    --band-b: #3073a4;
    --white: #ffffff;
    --ink: #111111;
    --glow: #c9f4ff;
    --icon: #1eb2e6;
  }
  * { margin: 0; padding: 0; box-sizing: border-box; }
  html, body { width: 1200px; height: 1091px; overflow: hidden; background: var(--mat); }
  body { position: relative; font-family: "Montserrat", sans-serif; }

  .flier {
    position: absolute; left: 298px; top: 155px; width: 603px; height: 779px;
    overflow: hidden; background: var(--sky);
  }
  .header {
    position: absolute; left: 0; top: 0; width: 100%; height: 110px;
    background: linear-gradient(90deg, var(--header-a), var(--header-b));
    box-shadow: 0 8px 14px rgba(0,0,0,0.35); z-index: 2;
  }
  .brand-mark {
    position: absolute; left: 58px; top: 30px; width: 49px; height: 49px;
    background: var(--white);
  }
  .brand-name {
    position: absolute; left: 118px; top: 36px;
    color: var(--white); font-weight: 700; font-size: 18.5px; letter-spacing: 0.8px;
  }
  .brand-tagline {
    position: absolute; left: 118px; top: 60px;
    color: var(--white); font-weight: 400; font-size: 12.6px; letter-spacing: 0.4px;
  }

  .hero {
    position: absolute; left: 0; top: 110px; width: 100%; height: 253px;
    background: linear-gradient(180deg, var(--sky), var(--sky-deep));
  }
  .hero-copy { position: absolute; left: 38px; top: 68px; color: var(--white); font-weight: 300; }
  .hero-copy .lead { font-size: 22px; letter-spacing: 0.5px; margin-bottom: 6px; }
  .hero-copy .big { font-size: 32px; line-height: 40px; letter-spacing: 1.2px; font-weight: 400; }
  .hero-copy .today { font-size: 26px; letter-spacing: 1px; margin-top: 6px; font-weight: 400; }

  .arrival {
    position: absolute; left: 0; top: 363px; width: 100%; height: 228px;
    background: linear-gradient(90deg, var(--slate), var(--sky-deep) 70%, var(--sky));
  }
  .arrival-copy {
    position: absolute; left: 38px; top: 40px; color: var(--white);
    font-size: 28px; line-height: 36px; font-weight: 400; letter-spacing: 0.6px;
  }

  .photo { position: absolute; border-radius: 50%; z-index: 3; }
  .photo-beach { left: 350px; top: 93px; width: 304px; height: 304px;
    background: linear-gradient(180deg, #3b6fd8 0%, #5b8d5a 35%, #b8a68a 70%, #c9b394 100%); }
  .photo-garden { left: 268px; top: 267px; width: 188px; height: 188px; z-index: 4;
    background: linear-gradient(180deg, #6c8a5a 0%, #d9d9d4 45%, #b23a3a 75%, #3b3b46 100%); }
  .photo-shore { left: 402px; top: 373px; width: 200px; height: 200px; z-index: 5;
    background: linear-gradient(180deg, #dfe8f0 0%, #6d8fa6 40%, #9fd4c9 70%, #7fc9b8 100%); }

  .pay-band {
    position: absolute; left: 0; top: 591px; width: 100%; height: 188px;
    background: linear-gradient(180deg, var(--band-a), var(--band-b));
  }
  .pay-line {
    position: absolute; left: 0; top: 28px; width: 100%; text-align: center;
    font-family: "PT Sans", sans-serif; font-weight: 700; font-size: 41px;
    color: var(--glow); -webkit-text-stroke: 1px #1b6a9a;
    text-shadow: 0 0 3px #e8fbff, 2px 2px 2px rgba(0,0,60,0.4);
  }
  .contact-pill {
    position: absolute; left: 29px; top: 107px; width: 544px; height: 48px;
    background: var(--white); border: 2px solid #1a4a6e; border-radius: 24px;
    display: flex; align-items: center; justify-content: center; gap: 10px;
    font-weight: 700; font-size: 19px; color: var(--ink);
  }
  .contact-pill svg { display: block; }
  .contact-item { display: flex; align-items: center; gap: 8px; }
</style>
</head>
<body>
  <main class="flier">
    <header class="header">
      <div class="brand-mark"></div>
      <div class="brand-name">GLOBAL YOUTH HOMESTAYS</div>
      <div class="brand-tagline">Welcoming American Homes for Young Travelers Worldwide</div>
    </header>

    <section class="hero">
      <div class="hero-copy">
        <p class="lead">Become a host for an</p>
        <p class="big">INTERNATIONAL<br>STUDENT</p>
        <p class="today">TODAY!</p>
      </div>
    </section>

    <section class="arrival">
      <p class="arrival-copy">International<br>students attending<br>BPIS<br>arriving NOW!</p>
    </section>

    <div class="photo photo-beach" role="img" aria-label="Photo of a host mother and students posing on a sunny beach"></div>
    <div class="photo photo-garden" role="img" aria-label="Photo of three students standing together outdoors"></div>
    <div class="photo photo-shore" role="img" aria-label="Photo of a host and a student by the water"></div>

    <section class="pay-band">
      <p class="pay-line">Hosts paid $1000/month</p>
      <div class="contact-pill">
        <span class="contact-item">
          <svg width="30" height="24" viewBox="0 0 30 24" aria-hidden="true">
            <path d="M2 8 Q15 0 28 8 L26 11 L21 10 L20 7 Q15 5 10 7 L9 10 L4 11 Z" fill="var(--icon)"/>
            <path d="M8 11 L22 11 L26 22 L4 22 Z" fill="var(--icon)"/>
            <g fill="#fff"><circle cx="12" cy="15" r="1"/><circle cx="15" cy="15" r="1"/><circle cx="18" cy="15" r="1"/><circle cx="12" cy="18" r="1"/><circle cx="15" cy="18" r="1"/><circle cx="18" cy="18" r="1"/></g>
          </svg>
          555-014-2290
        </span>
        <span class="contact-item">
          <svg width="24" height="24" viewBox="0 0 24 24" aria-hidden="true">
            <g fill="none" stroke="var(--icon)" stroke-width="2">
              <circle cx="12" cy="12" r="10"/><ellipse cx="12" cy="12" rx="4.5" ry="10"/>
              <line x1="2" y1="12" x2="22" y2="12"/><line x1="4" y1="7" x2="20" y2="7"/><line x1="4" y1="17" x2="20" y2="17"/>
            </g>
          </svg>
          www.globalyouthstays.com
        </span>
      </div>
    </section>
  </main>
</body>
</html>
```